Vorsa -Letter Head

We are predominantly a residential home builder based in Melbourne, Victoria Australia. We construct houses, apartments, townhouses, multi-unit developments.

The name of the company is "Vorsa"
My company believes in building unique construction projects mainly residential homes. The target customers are upmarket Melbourne residents/investors.

I want the brand name "Vorsa" to be part of the logo. There's no need to put the word construction in the logo at this stage.

I would also like some ideas for a slogan. But I would like something unique and different for a slogan not the same old cliche.

Industry/Entity Type

Construction

Requirements
Must have
• I need to be able to print quotes, general letters for customers, print tables and pictures on the letter head. So it must not have too much graphics and should be simple.

```html
<!DOCTYPE html>
<html lang="en">
<head>
<meta charset="utf-8">
<title>Vorsa Letterhead</title>
<link rel="stylesheet" href="https://fonts.googleapis.com/css2?family=Raleway:wght@400;500;600&display=swap">
<style>
  :root {
    --backdrop: #d8d8d8;
    --paper: #f1f1f1;
    --navy: #3b3a51;
    --cyan: #35b0d4;
    --white: #ffffff;
  }
  * { margin: 0; padding: 0; box-sizing: border-box; }
  html, body {
    width: 1200px;
    height: 968px;
    overflow: hidden;
    background: var(--backdrop);
    font-family: "Raleway", sans-serif;
  }
  .letterhead {
    position: absolute;
    left: 282px;
    top: 34px;
    width: 636px;
    height: 900px;
    background: var(--paper);
    box-shadow: 0 2px 10px rgba(0,0,0,0.12);
    overflow: hidden;
  }
  .header-shapes {
    position: absolute;
    left: 0;
    top: 0;
    width: 636px;
    height: 130px;
  }
  .brand-name {
    position: absolute;
    left: 40px;
    top: 20px;
    font-weight: 600;
    font-size: 40px;
    letter-spacing: 1px;
    color: var(--cyan);
    line-height: 1;
  }
  .contact-line {
    position: absolute;
    left: 222px;
    top: 80px;
    width: 400px;
    height: 42px;
    display: flex;
    align-items: center;
    justify-content: flex-end;
    gap: 14px;
    color: var(--white);
    font-size: 8.5px;
    font-weight: 500;
    letter-spacing: 0.2px;
  }
  .contact-item {
    display: flex;
    align-items: center;
    gap: 4px;
    white-space: nowrap;
  }
  .contact-icon { width: 9px; height: 9px; }
</style>
</head>
<body>
  <main class="letterhead">
    <svg class="header-shapes" viewBox="0 0 636 130" aria-hidden="true">
      <polygon points="0,0 272,0 226,80 0,80" fill="var(--navy)"/>
      <polygon points="226,80 636,80 636,122 202,122" fill="var(--cyan)"/>
    </svg>

    <div class="brand-name">Vorsa</div>

    <div class="contact-line">
      <span class="contact-item">118 Carrow St, Richmond VIC 3121</span>
      <span class="contact-item">
        <svg class="contact-icon" viewBox="0 0 10 10"><circle cx="5" cy="5" r="4.4" fill="none" stroke="#fff" stroke-width="0.9"/><path d="M3.4 2.8 L4.3 2.8 L4.7 4 L4.1 4.5 Q4.7 5.6 5.6 6 L6.1 5.4 L7.2 5.8 L7.2 6.7 Q5.2 7 3.3 4.1 Z" fill="#fff"/></svg>
        03-9420-5518
      </span>
      <span class="contact-item">
        <svg class="contact-icon" viewBox="0 0 10 10"><circle cx="5" cy="5" r="4.4" fill="none" stroke="#fff" stroke-width="0.9"/><rect x="2.8" y="3.4" width="4.4" height="3.2" fill="none" stroke="#fff" stroke-width="0.7"/><path d="M2.8 3.4 L5 5.2 L7.2 3.4" fill="none" stroke="#fff" stroke-width="0.7"/></svg>
        info@vorsa.com
      </span>
      <span class="contact-item">
        <svg class="contact-icon" viewBox="0 0 10 10"><circle cx="5" cy="5" r="4.4" fill="none" stroke="#fff" stroke-width="0.9"/><ellipse cx="5" cy="5" rx="1.6" ry="3.4" fill="none" stroke="#fff" stroke-width="0.6"/><line x1="1.6" y1="5" x2="8.4" y2="5" stroke="#fff" stroke-width="0.6"/></svg>
        www.vorsa.com
      </span>
    </div>
  </main>
</body>
</html>
```